依頼詳細
カキ氷店を新規オープンする企業です。
当社商品の特徴をわかりやすく、魅力的に表現にして頂きたく募集致しました。
誰もが理解できるわかりやすいデザインのご提案をお願い致します。

1、チャレンジかき氷(手動のカキ氷機でお客様自身にカキ氷を製造して頂きます。)
・カキ氷専用の氷を使用します。(通常なら48時間で「純氷」となるところを、さらに長い72時間かけてじっくりと凍らせたかき氷専用の氷)

2、ふわとろカキ氷(台湾カキ氷)
(こちらの商品は製造してご提供致します。)
・フルーツ含有量90%の高級果実ピューレと共にお召し上がり頂きます。
記載項目
看板(横断幕)の記載内容は下記になります。
■看板(横断幕)サイズ、縦1200mm:横3000mm(多少の変更あり)
■店名、汐凪カキ氷本舗
■依頼詳細の1、2の内容
■カキ氷の画像
・チャレンジかき氷はカキ氷機の画像(添付画像①あり)
・ふわとろカキ氷(台湾カキ氷)の画像(参考添付画像②あり)
・上記2点の画像はサイズの大きいタイプの用意ができませんので、CG、イラストで問題ございません。

※店前に添付画像③のような立て看板(幕)も設置致しますので、上記と同様の内容でご提案頂けますようお願い致します。
■看板(幕)サイズ、縦2000mm:横1200mm(多少の変更あり)
希望イメージ
シンプル 複雑
単色 カラフル
暗い 明るい
日常 高級
遊び心 厳粛
未来的 伝統的
女性的 男性的
希望する色
青系、水色系
納品ファイル
• 高解像度JPG (.jpg)
• イラストレーター形式 (.ai)
補足説明
納品データは、aiでお願い致します。
納品以前のご提案は、Jpgでお願い致します。
デザインを依頼している看板(横断幕)のサイズが決定致しました。
サイズ:縦1800mm:横4000mmで決定致しましたのでご提案お願い致します。

同様に立て看板(幕)のサイズも縦2000mm:横1200mmで決定致しましたのでご提案お願い致します。

立て看板のデザインに関しては、横断幕と内容が同じであれば、違うデザインでもOKです。
古風・和・高級感・シンプルをイメージするようなデザインをご提案して頂く事は可能でしょうか?

使用する横断幕は、下記URLのショップで発注予定です。
http://www.kelsaro.net/html/service/ou1.html
ふわとろカキ氷の商品イメージ画像を新たに添付致しますのでご確認下さい。
商品画像イメージ1’・2’をアップ致しました。
募集を延期致しました。
カキ氷の追加画像です。
今回アップしたサイズが最大の画像になります。

当社の依頼内容が最も反映されたデザインだったから。
また追記の内容にも即座に反応して頂けたから。
当選のクリフォ様のご対応が迅速且つ大変丁寧だったから。
最終的に好みだったから。

この度は、当社の看板デザイン募集にたくさんご応募頂き、誠にありがとうございました。
また看板デザインという大変な作業にも関わらず、本当にご応募頂きありがとうございました。
またクリフォンでお仕事を依頼させて頂きますので今後とも宜しくお願い致します。
この度は、誠にありがとうございました。

```html
<!DOCTYPE html>
<html lang="ja">
<head>
<meta charset="utf-8">
<title>汐凪カキ氷本舗</title>
<link href="https://fonts.googleapis.com/css2?family=Kaisei+Decol:wght@700&family=Zen+Antique+Soft&family=Zen+Maru+Gothic:wght@700&display=swap" rel="stylesheet">
<style>
  :root {
    --bg-deep: #5b4f9c;
    --bg-mid: #7a70b8;
    --bg-light: #b3acd8;
    --frame: #e9e4f6;
    --moon: #8fa6dd;
    --moon-light: #b7c6ee;
    --scroll-paper: #fbf1cf;
    --scroll-gold: #d2a23c;
    --scroll-edge: #9a6a1c;
    --ink: #2a1c12;
    --title-fill: #ffffff;
    --title-stroke: #1d2a6b;
    --note-ink: #1e1640;
    --machine: #7fc2ae;
    --ice: #f5b52e;
    --flower: #e7873a;
  }
  html, body { margin: 0; padding: 0; overflow: hidden; }
  body { width: 720px; height: 1200px; background: #fff; }
  .sign {
    position: relative; width: 720px; height: 1200px; overflow: hidden;
    background: linear-gradient(180deg, var(--bg-mid) 0%, var(--bg-light) 45%, var(--bg-mid) 75%, var(--bg-deep) 100%);
  }
  .frame {
    position: absolute; inset: 14px; border: 3px solid var(--frame); pointer-events: none;
  }
  .moon {
    position: absolute; left: 226px; top: 358px; width: 340px; height: 340px; border-radius: 50%;
    background: radial-gradient(circle at 45% 40%, var(--moon-light), var(--moon) 70%);
  }
  .art { position: absolute; }
  .machine-art {
    left: 30px; top: 40px; width: 330px; height: 420px; border-radius: 18px;
    background: linear-gradient(160deg, #a6d9c9, var(--machine));
  }
  .ice-art {
    left: 300px; top: 790px; width: 290px; height: 360px; border-radius: 140px 140px 30px 30px;
    background: radial-gradient(circle at 50% 40%, #ffd46a, var(--ice) 75%);
  }
  .flower { border-radius: 50%; background: radial-gradient(circle, #f6c15a, var(--flower) 70%); }
  .flower-tl { left: -40px; top: -40px; width: 170px; height: 170px; }
  .flower-mr { right: -40px; top: 720px; width: 150px; height: 150px; }
  .flower-br { right: -50px; bottom: -50px; width: 220px; height: 220px; }

  .scroll {
    position: absolute; width: 92px; padding: 24px 0;
    background: var(--scroll-paper);
    border-left: 8px solid var(--scroll-gold); border-right: 8px solid var(--scroll-gold);
    box-sizing: border-box;
    display: flex; justify-content: center; align-items: center;
  }
  .scroll::before, .scroll::after {
    content: ""; position: absolute; left: -14px; right: -14px; height: 16px;
    background: var(--scroll-gold); border: 2px solid var(--scroll-edge); border-radius: 8px;
  }
  .scroll::before { top: -8px; }
  .scroll::after { bottom: -8px; }
  .scroll-title {
    writing-mode: vertical-rl; margin: 0; white-space: nowrap;
    font-family: "Zen Antique Soft", serif; font-size: 44px; line-height: 1; color: var(--ink); letter-spacing: 2px;
  }
  .scroll-challenge { left: 566px; top: 44px; height: 470px; }
  .scroll-fuwatoro { left: 50px; top: 722px; height: 430px; }

  .note {
    position: absolute; margin: 0; writing-mode: vertical-rl; white-space: nowrap;
    font-family: "Zen Maru Gothic", sans-serif; font-weight: 700; font-size: 30px; line-height: 1.3;
    color: var(--note-ink); letter-spacing: 1px;
  }
  .note-challenge { left: 456px; top: 50px; }
  .note-fuwatoro { left: 190px; top: 722px; }

  .shop-name {
    position: absolute; left: 0; right: 0; top: 520px; margin: 0; text-align: center;
    font-family: "Kaisei Decol", serif; font-weight: 700; color: var(--title-fill);
    -webkit-text-stroke: 6px var(--title-stroke); paint-order: stroke fill;
    line-height: 1.1;
  }
  .shop-name .line1 { display: block; font-size: 80px; letter-spacing: 8px; }
  .shop-name .line2 { display: block; font-size: 84px; letter-spacing: 2px; }
</style>
</head>
<body>
<main class="sign">
  <div class="frame"></div>
  <div class="moon"></div>

  <div class="art flower flower-tl" role="img" aria-label="菊の花の飾り"></div>
  <div class="art flower flower-mr" role="img" aria-label="菊の花の飾り"></div>
  <div class="art flower flower-br" role="img" aria-label="菊の花の飾り"></div>

  <div class="art machine-art" role="img" aria-label="手回し式のかき氷機のイラスト"></div>

  <div class="scroll scroll-challenge"><h2 class="scroll-title">チャレンジかき氷</h2></div>
  <p class="note note-challenge">熟成した専用の氷を<br>自身でつくって食す!</p>

  <h1 class="shop-name"><span class="line1">汐凪</span><span class="line2">カキ氷本舗</span></h1>

  <div class="scroll scroll-fuwatoro"><h2 class="scroll-title">ふわとろカキ氷</h2></div>
  <p class="note note-fuwatoro">フルーツ含有量90%<br>高級果実ピューレで食す!</p>

  <div class="art ice-art" role="img" aria-label="マンゴー色のふわとろカキ氷の写真"></div>
</main>
</body>
</html>
```